I want a double sided flyer possibly with a picture of a lawn or grass.
Company name, phone number, email, and logo
Halvorsen Turf Management, (404)726-1853,Halvorsen_Turf@brevimail.com
Company services
Fertilization and weed control,Lawn and Landscape maintenance, mowing, pruning, aeration, landscape and Christmas lights,

```html
<!DOCTYPE html>
<html lang="en">
<head>
<meta charset="utf-8">
<title>Halvorsen Turf Management – Flyer</title>
<link rel="stylesheet" href="https://fonts.googleapis.com/css2?family=PT+Sans+Narrow:wght@400;700&family=Open+Sans:wght@400&display=swap">
<style>
  :root {
    --backdrop: #ebebeb;
    --card: #ffffff;
    --green: #3c9a2c;
    --green-bright: #5cb531;
    --green-pale: #d8ecb0;
    --ink: #4a4a4a;
    --ink-soft: #555555;
    --rule: #c9c9c9;
  }
  * { box-sizing: border-box; margin: 0; padding: 0; }
  html, body {
    width: 1200px; height: 900px; overflow: hidden;
    background: var(--backdrop);
  }
  .canvas { position: relative; width: 1200px; height: 900px; }

  /* Front side */
  .front {
    position: absolute; left: 37px; top: 244px;
    width: 559px; height: 374px;
    background: var(--card);
    display: flex; align-items: center; justify-content: center;
  }
  .brand-name {
    font-family: "PT Sans Narrow", sans-serif;
    font-weight: 700;
    color: var(--green);
    text-align: left;
    line-height: 1;
  }
  .brand-name .primary { display: block; font-size: 50px; letter-spacing: 1px; }
  .brand-name .secondary { display: block; font-size: 21px; margin-top: 4px; }

  /* Back side */
  .back {
    position: absolute; left: 641px; top: 247px;
    width: 527px; height: 371px;
    background: var(--card);
  }
  .lawn-photo {
    position: absolute; left: 0; top: 0; width: 527px; height: 327px;
    background:
      radial-gradient(ellipse at 90% 20%, #a8d44a 0%, rgba(168,212,74,0) 45%),
      linear-gradient(180deg, #f6f9ec 0%, #e4f0c4 45%, #a9d85a 68%, #5fb52a 85%, #3f9a1e 100%);
  }
  .slogan {
    position: absolute; right: 351px; top: 92px;
    font-family: "PT Sans Narrow", sans-serif;
    text-align: right; line-height: 0.92;
    color: var(--ink);
    text-transform: uppercase;
  }
  .slogan .s1 { display: block; font-size: 31px; }
  .slogan .s2 { display: block; font-size: 46px; }
  .slogan .s3 { display: block; font-size: 33px; }
  .slogan .s4 { display: block; font-size: 44px; color: var(--green); }

  .services {
    position: absolute; left: 195px; top: 81px;
    width: 301px; height: 162px;
  }
  .services-bar {
    position: absolute; left: 0; top: 0; width: 11px; height: 162px;
    background: var(--green);
  }
  .services-panel { position: absolute; left: 11px; top: 0; }
  .services-body { position: absolute; left: 30px; top: 12px; }
  .services-title {
    font-family: "PT Sans Narrow", sans-serif;
    font-size: 20px; color: var(--green); font-weight: 400;
    margin-bottom: 3px;
  }
  .services-list { list-style: none; }
  .services-list li {
    font-family: "Open Sans", sans-serif;
    font-size: 11.5px; color: #333; line-height: 20px;
    padding-left: 13px; position: relative;
  }
  .services-list li::before {
    content: ""; position: absolute; left: 0; top: 8px;
    width: 5px; height: 5px; border-radius: 50%;
    background: var(--green-bright);
  }

  .contact-strip {
    position: absolute; left: 0; top: 331px; width: 527px; height: 40px;
    display: flex; align-items: center;
  }
  .name-tag {
    position: relative; width: 217px; height: 40px; flex: none;
  }
  .name-tag svg { position: absolute; inset: 0; }
  .name-tag span {
    position: absolute; left: 26px; top: 0; line-height: 40px;
    font-family: "PT Sans Narrow", sans-serif; font-size: 15px; color: #fff;
  }
  .contact-item {
    display: flex; align-items: center; gap: 6px;
    font-family: "PT Sans Narrow", sans-serif; color: var(--ink-soft);
  }
  .contact-email { margin-left: 2px; font-size: 13.5px; }
  .contact-divider { width: 1px; height: 22px; background: var(--rule); margin: 0 8px; }
  .contact-phone { font-size: 17px; }
</style>
</head>
<body>
<main class="canvas">

  <section class="front" aria-label="Flyer front">
    <h1 class="brand-name">
      <span class="primary">HALVORSEN</span>
      <span class="secondary">Turf Management</span>
    </h1>
  </section>

  <section class="back" aria-label="Flyer back">
    <div class="lawn-photo" role="img" aria-label="Photograph of fresh green grass against a bright, softly blurred sunny background"></div>

    <p class="slogan">
      <span class="s1">We</span>
      <span class="s2">Care</span>
      <span class="s3">For your</span>
      <span class="s4">Yard!</span>
    </p>

    <div class="services">
      <div class="services-bar"></div>
      <svg class="services-panel" width="290" height="162" viewBox="0 0 290 162" aria-hidden="true">
        <polygon points="0,0 270,0 290,24 290,162 0,162" fill="#ffffff" fill-opacity="0.55"/>
      </svg>
      <div class="services-body">
        <h2 class="services-title">COMPANY SERVICES</h2>
        <ul class="services-list">
          <li>Fertilization and weed control</li>
          <li>Lawn and Landscape maintenance</li>
          <li>Mowing</li>
          <li>Pruning</li>
          <li>Aeration</li>
          <li>Landscape and Christmas lights</li>
        </ul>
      </div>
    </div>

    <div class="contact-strip">
      <div class="name-tag">
        <svg width="217" height="40" viewBox="0 0 217 40" aria-hidden="true">
          <polygon points="0,0 195,0 217,40 0,40" fill="#3c9a2c"/>
        </svg>
        <span>Halvorsen Turf Management</span>
      </div>
      <div class="contact-item contact-email">
        <svg width="20" height="14" viewBox="0 0 20 14" aria-hidden="true">
          <rect x="1" y="1" width="18" height="12" fill="none" stroke="#3c9a2c" stroke-width="1.6"/>
          <polyline points="1,1 10,8 19,1" fill="none" stroke="#3c9a2c" stroke-width="1.6"/>
        </svg>
        <span>Halvorsen_Turf@brevimail.com</span>
      </div>
      <div class="contact-divider"></div>
      <div class="contact-item contact-phone">
        <svg width="20" height="20" viewBox="0 0 20 20" aria-hidden="true">
          <circle cx="10" cy="10" r="9" fill="none" stroke="#3c9a2c" stroke-width="1.6"/>
          <path d="M7 5.5 L8.6 7.8 L7.6 9 Q8.6 11.4 11 12.4 L12.2 11.4 L14.5 13 L13.4 14.6 Q9.5 15 6.6 11.6 Q5 9 5.6 6.6 Z" fill="#3c9a2c"/>
        </svg>
        <span>(404)726-1853</span>
      </div>
    </div>
  </section>

</main>
</body>
</html>
```